Recruitment of Brackwell Staffing for the UK market

I want a website for the UK market to attract businesses and companies to come to us for Philipine labour. We want an information site that gives all information on what we do and how we can recruit Philippine labour.
This is a recruitment site for companies to contact us with their requirements for skilled workers coming from the Philipines over to the UK to work.

Target Market(s)

Uk Companies and businesses who want Philipine skilled workers

Industry/Entity Type

REcruitment

Coding

Coded - Design and coding required

Number of Pages Required

5+ page

Font styles to use
Sans Serif

Colors
0054AA
0677BA
7BADD7
CADEEF
E8F1F8
0094D4
00A9DD
6FCCEA
C7EBF8
E9F6FB
EE7325
F08F49
F5BC92
FAE3D3
FDF4ED
EB3D1F
EC4F4E
F09395
F8D3D4
FCEDEE

Requirements
Must have
• Look professional and corperate with drop down menus for Home ,about, services,articles. training , contact us
Nice to have
• Look at Tolvery recruitment- https://tolveryrecruitment.example.co.uk/. This is my current site - https://www.brackwellstaffing.example.com/
Should not have
• Cartoons or silly pictures , needs to be corperate looking

```html
<!DOCTYPE html>
<html lang="en">
<head>
<meta charset="utf-8">
<title>Brackwell Staffing – Skilled Philippine Workers for UK Companies</title>
<link href="https://fonts.googleapis.com/css2?family=Roboto:wght@400;500;700&display=swap" rel="stylesheet">
<style>
:root{
  --brand:#9b2b2b;
  --brand-dark:#7f2020;
  --ink:#1d1d1d;
  --muted:#6f6f6f;
  --soft:#9a9a9a;
  --grey-band:#f2f2f2;
  --black:#000;
  --map-blue:#8eaef0;
  --white:#fff;
  --line:#d9d9d9;
}
*{box-sizing:border-box;margin:0;padding:0}
html,body{width:1200px;height:4890px;overflow:hidden}
body{font-family:'Roboto',Arial,sans-serif;color:var(--ink);background:var(--white);position:relative}
.abs{position:absolute}
a{color:inherit;text-decoration:none}

/* top bar */
.topbar{left:0;top:0;width:1200px;height:38px;background:var(--brand);color:var(--white);font-size:13px}
.topbar .contact{position:absolute;right:84px;top:11px;display:flex;gap:16px;align-items:center}
.topbar span{display:flex;gap:6px;align-items:center}

/* header */
.brand-name{font-weight:700;color:var(--brand);font-size:28px;letter-spacing:.5px}
.header-logo{left:76px;top:70px;display:flex;align-items:center;gap:10px}
.logo-square{width:26px;height:26px;background:var(--brand)}
.nav{left:399px;top:82px;display:flex;gap:42px;font-size:14px;color:#333}
.nav .active{border-bottom:2px dotted var(--brand);padding-bottom:4px}
.nav .drop::after{content:" ▾";font-size:9px;color:#888}
.btn{display:inline-flex;align-items:center;justify-content:center;background:var(--brand);color:var(--white);font-weight:500;border-radius:30px;text-transform:uppercase}
.btn-jobs{left:976px;top:72px;width:141px;height:42px;font-size:13px;font-weight:700}

/* hero */
.hero-title{left:148px;top:262px;width:460px;font-size:38px;font-weight:700;line-height:46px}
.hero-text{left:148px;top:420px;width:420px;font-size:13px;line-height:19px;color:#333}
.btn-hero{left:148px;top:503px;width:222px;height:46px;font-size:16px}
.hero-photo{left:612px;top:215px;width:436px;height:436px;border-radius:50%;background:radial-gradient(circle at 55% 35%,#f1d7b9,#c9cfd8 55%,#e8eef4)}

/* industries */
.section-title{font-size:32px;font-weight:500;text-align:center;width:1200px;left:0}
.industry{top:932px;width:258px;height:175px;border-radius:6px;overflow:hidden}
.industry .label{position:absolute;left:20px;bottom:12px;color:var(--white);font-size:22px;font-weight:700}
.dots{left:553px;top:1151px;display:flex;gap:10px}
.dots i{width:10px;height:10px;border-radius:50%;background:#ccc;display:block}
.dots i:first-child{background:#111}

/* opportunities */
.grey-band{left:0;top:1202px;width:1200px;height:1016px;background:var(--grey-band)}
.job{left:152px;width:896px;height:165px;background:var(--white);border-radius:6px;box-shadow:0 2px 10px rgba(0,0,0,.06)}
.job .thumb{position:absolute;left:20px;top:22px;width:164px;height:121px;border-radius:4px}
.job .info{position:absolute;left:212px;top:50px;font-size:12px;color:var(--soft);line-height:18px}
.job .info h3{font-size:15px;color:var(--ink);font-weight:500;margin-bottom:4px}
.job .divider{position:absolute;left:392px;top:35px;width:1px;height:95px;background:var(--line)}
.job .desc{position:absolute;left:420px;top:55px;width:300px;font-size:11px;line-height:14px;color:#444}
.job .actions{position:absolute;left:754px;top:48px;display:flex;flex-direction:column;gap:10px}
.pill{width:100px;height:34px;border-radius:20px;font-size:11px;font-weight:700;display:flex;align-items:center;justify-content:center;text-transform:uppercase}
.pill.outline{border:2px solid var(--brand);color:var(--brand)}
.pill.solid{background:var(--brand);color:var(--white)}
.pager{left:524px;top:2134px;display:flex;gap:20px;font-size:14px;color:#444}
.pager .current{color:var(--brand);font-weight:700}

/* workers */
.role-label{font-size:17px;font-weight:500;color:#222;text-align:center;width:258px}
.worker{width:258px;height:240px}
.eyebrow{font-size:14px;font-weight:500;text-transform:uppercase;color:#888}
.people-title{left:648px;top:2420px;width:460px;font-size:44px;font-weight:500;line-height:52px}
.people-text{left:652px;top:2548px;width:405px;font-size:14px;line-height:24px;color:#555}
.btn-more{left:650px;top:2736px;width:220px;height:48px;font-size:17px}

/* help / do */
.split{left:0;top:2959px;width:1200px;height:532px;background:var(--black)}
.split h2{font-size:42px;font-weight:500;color:var(--white)}
.split p{font-size:14px;line-height:22.5px;color:var(--white)}
.help{left:150px;top:3112px;width:380px}
.do{left:697px;top:3112px;width:380px}
.split h2{margin-bottom:22px}

/* blog */
.post{top:3704px;width:250px}
.post .date{font-size:13px;font-weight:700;color:var(--brand)}
.post h3{font-size:18px;line-height:23px;font-weight:700;margin:20px 0 14px}
.post p{font-size:12px;line-height:19px;color:#888}

/* map band */
.map-band{left:0;top:4022px;width:1200px;height:444px;background:var(--map-blue)}
.map-art{left:110px;top:4040px;width:470px;height:420px;background:linear-gradient(160deg,#a9c0ef,#b7c9e6 50%,#9eb6ec)}
.together{left:648px;top:4160px;width:470px;color:var(--white)}
.together .eyebrow{color:var(--white);font-size:19px}
.together p{font-size:27px;line-height:34px;margin-top:22px}

/* footer */
.footer-logo{left:152px;top:4532px;display:flex;align-items:center;gap:10px}
.footer-about{left:150px;top:4596px;width:330px;font-size:11px;line-height:18px;color:#555}
.socials{left:146px;top:4697px;display:flex;gap:16px}
.socials i{display:block;width:44px;height:44px;border:2px solid #222;border-radius:50%}
.footer-col h4{font-size:22px;font-weight:500;margin-bottom:22px}
.footer-col li{list-style:none;font-size:13px;color:#444;line-height:24px;display:flex;gap:10px;align-items:flex-start}
.footer-col li svg{margin-top:5px;flex:none}
.contact-col{left:547px;top:4515px;width:320px}
.links-col{left:902px;top:4515px}
.links-col li{line-height:24px}
.footer-rule{left:156px;top:4793px;width:885px;height:1px;background:#999}
.copyright{left:0;top:4818px;width:1200px;text-align:center;font-size:12px;color:#333}
</style>
</head>
<body>

<header>
  <div class="abs topbar">
    <div class="contact">
      <span><svg width="12" height="12" viewBox="0 0 24 24" fill="#fff"><path d="M6.6 10.8a15 15 0 006.6 6.6l2.2-2.2a1 1 0 011-.25 11.4 11.4 0 003.6.57 1 1 0 011 1V20a1 1 0 01-1 1A17 17 0 013 4a1 1 0 011-1h3.5a1 1 0 011 1c0 1.25.2 2.45.57 3.57a1 1 0 01-.25 1z"/></svg>07700 900418</span>
      <span><svg width="13" height="10" viewBox="0 0 24 18" fill="#fff"><path d="M0 0h24v18H0z" opacity=".0"/><path d="M1 1h22v16H1z" fill="#fff"/><path d="M1 1l11 8 11-8" stroke="#9b2b2b" stroke-width="2" fill="none"/></svg>sales@brackwellstaffing.example.com</span>
    </div>
  </div>

  <div class="abs header-logo"><div class="logo-square"></div><span class="brand-name">Brackwell Staffing</span></div>

  <nav class="abs nav">
    <a class="active">Home</a><a>About</a><a class="drop">Services</a><a>Articles</a><a class="drop">Training</a><a>Contact Us</a>
  </nav>
  <a class="abs btn btn-jobs">Jobs near me</a>
</header>

<section class="hero">
  <h1 class="abs hero-title">Recruiting and placing skilled Philippine workers into UK companies</h1>
  <p class="abs hero-text">Lorem ipsum dolor sit amet, consectetur adipiscing elit, sed do eiusmod tempor incididunt ut labo na aliquis ipsum.</p>
  <a class="abs btn btn-hero">Contact us today</a>
  <svg class="abs" style="left:590px;top:178px" width="500" height="510" viewBox="0 0 500 510">
    <path d="M330 20 A247 247 0 1 1 60 420" fill="none" stroke="var(--brand)" stroke-width="5"/>
  </svg>
  <div class="abs hero-photo" role="img" aria-label="Smiling construction worker in a yellow hard hat with a female colleague"></div>
</section>

<section class="industries">
  <h2 class="abs section-title" style="top:845px">Find Talent in Your Industry</h2>
  <div class="abs industry" style="left:61px;background:linear-gradient(160deg,#8d8a86,#c46a3a 60%,#6e5b4b)" role="img" aria-label="Engineers in safety gear at work"><span class="label">Engineers</span></div>
  <div class="abs industry" style="left:334px;background:linear-gradient(160deg,#cfe3ea,#8fb7c2 60%,#5d7f8b)" role="img" aria-label="Healthcare team in uniforms"><span class="label">Health Care</span></div>
  <div class="abs industry" style="left:607px;background:linear-gradient(160deg,#4b5474,#2e3550 60%,#8a6d5a)" role="img" aria-label="Welder at work with sparks"><span class="label">Welders</span></div>
  <div class="abs industry" style="left:879px;background:linear-gradient(160deg,#e6a75a,#9a6a3a 55%,#3f352c)" role="img" aria-label="Construction workers on site at sunset"><span class="label">Construction</span></div>
  <div class="abs dots"><i></i><i></i><i></i><i></i><i></i></div>
</section>

<section class="opportunities">
  <div class="abs grey-band"></div>
  <h2 class="abs section-title" style="top:1244px">Opportunities | Across all locations</h2>

  <article class="abs job" style="top:1335px">
    <div class="thumb" role="img" aria-label="Doctor reviewing notes on a tablet" style="background:linear-gradient(135deg,#dfe6ea,#8fa5b3)"></div>
    <div class="info"><h3>Lorem ipsum dolor</h3>Location name: Philippine<br>Salary: 23 K &nbsp;&nbsp; Experience: 2 Y</div>
    <div class="divider"></div>
    <p class="desc">Lorem ipsum dolor sit amet, consectetur adipiscing elit, sed do eiusmod tempor incididunt ut labore et dolore magna aliqua. Quis ipsum suspendisse ultrices gravida. Risus commodo viverra maecenas accumsan</p>
    <div class="actions"><span class="pill outline">Read more</span><span class="pill solid">Apply now</span></div>
  </article>

  <article class="abs job" style="top:1523px">
    <div class="thumb" role="img" aria-label="Engineer working on machinery" style="background:linear-gradient(135deg,#3d5a80,#c97d4a)"></div>
    <div class="info"><h3>Lorem ipsum dolor</h3>Location name: Philippine<br>Salary: 23 K &nbsp;&nbsp; Experience: 2 Y</div>
    <div class="divider"></div>
    <p class="desc">Lorem ipsum dolor sit amet, consectetur adipiscing elit, sed do eiusmod tempor incididunt ut labore et dolore magna aliqua. Quis ipsum suspendisse ultrices gravida. Risus commodo viverra maecenas accumsan</p>
    <div class="actions"><span class="pill outline">Read more</span><span class="pill solid">Apply now</span></div>
  </article>

  <article class="abs job" style="top:1711px">
    <div class="thumb" role="img" aria-label="Site worker in hard hat and hi-vis vest" style="background:linear-gradient(135deg,#e9e4dc,#d08a3a 60%,#5a4a3e)"></div>
    <div class="info"><h3>Lorem ipsum dolor</h3>Location name: Philippine<br>Salary: 23 K &nbsp;&nbsp; Experience: 2 Y</div>
    <div class="divider"></div>
    <p class="desc">Lorem ipsum dolor sit amet, consectetur adipiscing elit, sed do eiusmod tempor incididunt ut labore et dolore magna aliqua. Quis ipsum suspendisse ultrices gravida. Risus commodo viverra maecenas accumsan</p>
    <div class="actions"><span class="pill outline">Read more</span><span class="pill solid">Apply now</span></div>
  </article>

  <article class="abs job" style="top:1905px">
    <div class="thumb" role="img" aria-label="Engineer in a server room" style="background:linear-gradient(135deg,#2b3d5a,#6b8fb5 60%,#1e2636)"></div>
    <div class="info"><h3>Civil Engineer</h3>Location name: Philippine<br>Salary: 23 K &nbsp;&nbsp; Experience: 2 Y</div>
    <div class="divider"></div>
    <p class="desc">Lorem ipsum dolor sit amet, consectetur adipiscing elit, sed do eiusmod tempor incididunt ut labore et dolore magna aliqua. Quis ipsum suspendisse ultrices gravida. Risus commodo viverra maecenas accumsan</p>
    <div class="actions"><span class="pill outline">Read more</span><span class="pill solid">Apply now</span></div>
  </article>

  <div class="abs pager"><span class="current">1</span><span>2</span><span>3</span><span>4......Last</span></div>
</section>

<section class="workers">
  <p class="abs role-label" style="left:63px;top:2285px">Site engineer</p>
  <p class="abs role-label" style="left:336px;top:2285px">Civil engineer</p>
  <div class="abs worker" style="left:63px;top:2336px;background:linear-gradient(150deg,#d9d9d2,#c9c44a 55%,#6a6a5e)" role="img" aria-label="Site engineers reviewing plans on a laptop"></div>
  <div class="abs worker" style="left:336px;top:2336px;background:linear-gradient(160deg,#b9c7d6,#7d8a97 55%,#4b5562)" role="img" aria-label="Civil engineer overlooking a building site"></div>
  <div class="abs worker" style="left:63px;top:2586px;background:linear-gradient(150deg,#e9e9e6,#b8b3ab 55%,#7f776c)" role="img" aria-label="Consultants meeting around a laptop"></div>
  <div class="abs worker" style="left:336px;top:2586px;background:linear-gradient(150deg,#3e4450,#8b95a5 55%,#1f242c)" role="img" aria-label="Developer checking equipment in a data centre"></div>
  <p class="abs role-label" style="left:63px;top:2848px">Web design consultant</p>
  <p class="abs role-label" style="left:336px;top:2848px">Internet developer</p>

  <p class="abs eyebrow" style="left:648px;top:2389px">UK skilled workers list</p>
  <h2 class="abs people-title">find the right people for your business</h2>
  <p class="abs people-text">The UK government since brexit have developed a new system based on points (similar to Australia) when recruiting from outside of the UK. Previously EU citizens could work in the UK without any extensive documentation or clarification of skills. This has all changed. Overseas recruitment must now focus on skills that are currently short in the UK. The list is extensive and is constantly being reviewed.</p>
  <a class="abs btn btn-more">More information</a>
</section>

<section class="abs split">
  <svg class="abs" style="left:0;top:0" width="640" height="532" viewBox="0 0 640 532">
    <polygon points="0,0 522,0 627,266 522,532 0,532" fill="var(--brand)"/>
    <polyline points="562,0 632,266 562,532" fill="none" stroke="#fff" stroke-width="2" opacity=".0"/>
  </svg>
  <div class="abs help" style="top:153px">
    <h2>How we help</h2>
    <p>We work with companies to find skilled workers that meet the UK requirements for Visas and work permits. We guide you through the whole process and deliver highly trained people that add value to your business. We are here to help both the companies and the Philippino people to gain a better standard of living for their families.</p>
  </div>
  <div class="abs do" style="top:153px">
    <h2>What We Do</h2>
    <p>Our company has been estabilished in the Philippines for over 20 years. We have mainly been recruiting philippine workers for the off shore industry in asia but since brexit and the new rules on skilled workers entering the UK we have been working with UK companies who now have chance to recruit some of the finest hard working talent from the Philippines for their companies..</p>
  </div>
</section>

<section class="blog">
  <h2 class="abs section-title" style="top:3604px;font-size:42px">Read our recent blog articles</h2>
  <article class="abs post" style="left:148px">
    <p class="date">23/ Apr / 2023</p>
    <h3>Lorem ipsum dolor sit amet, consectetur adipiscing elised do eiusmod tempor inci</h3>
    <p>Lorem ipsum dolor sit amet, consectetur adip iscing elit, sed do eiusmod tempor incididunt labore et dolore magna aliqua. Quis ipsum suspendisse ultrices gravidasus commodo viverra maecenas accumsan lacu</p>
  </article>
  <article class="abs post" style="left:458px">
    <p class="date">23/ Apr / 2023</p>
    <h3>Lorem ipsum dolor sit amet, consectetur adipiscing elised do eiusmod tempor inci</h3>
    <p>Lorem ipsum dolor sit amet, consectetur adip iscing elit, sed do eiusmod tempor incididunt labore et dolore magna aliqua. Quis ipsum suspendisse ultrices gravidasus commodo viverra maecenas accumsan lacu</p>
  </article>
  <article class="abs post" style="left:790px">
    <p class="date">23/ Apr / 2023</p>
    <h3>Lorem ipsum dolor sit amet, consectetur adipiscing elised do eiusmod tempor inci</h3>
    <p>Lorem ipsum dolor sit amet, consectetur adip iscing elit, sed do eiusmod tempor incididunt labore et dolore magna aliqua. Quis ipsum suspendisse ultrices gravidasus commodo viverra maecenas accumsan lacu</p>
  </article>
</section>

<section class="locations">
  <div class="abs map-band"></div>
  <div class="abs map-art" role="img" aria-label="Map of the Philippines with recruitment centres marked in red"></div>
  <div class="abs together">
    <p class="eyebrow">Working together</p>
    <p>We recruit the finest talent available with our dedicated 200 strong team. Our centres are highlighted in red dots on the map.</p>
  </div>
</section>

<footer>
  <div class="abs footer-logo"><div class="logo-square"></div><span class="brand-name">Brackwell Staffing</span></div>
  <p class="abs footer-about">We source skilled workers directly from the Philippines to work in the UK. With offices , training locations and specialist recruiters we can find the highest quality individuals to add value and resources to any UK business. We delivery quality based on vast experience over a number of years.</p>
  <div class="abs socials" aria-label="Social links"><i></i><i></i><i></i><i></i></div>

  <div class="abs footer-col contact-col">
    <h4>Contact Details</h4>
    <ul>
      <li><svg width="12" height="12" viewBox="0 0 24 24" fill="var(--brand)"><path d="M6.6 10.8a15 15 0 006.6 6.6l2.2-2.2a1 1 0 011-.25 11.4 11.4 0 003.6.57 1 1 0 011 1V20a1 1 0 01-1 1A17 17 0 013 4a1 1 0 011-1h3.5a1 1 0 011 1c0 1.25.2 2.45.57 3.57a1 1 0 01-.25 1z"/></svg>Phone: 07700 900418</li>
      <li style="margin-top:10px"><svg width="12" height="10" viewBox="0 0 24 18"><rect x="1" y="1" width="22" height="16" fill="var(--brand)"/><path d="M1 1l11 8 11-8" stroke="#fff" stroke-width="2" fill="none"/></svg>sales@brackwellstaffing.example.com</li>
      <li style="margin-top:10px;line-height:18px"><svg width="10" height="14" viewBox="0 0 20 28" fill="var(--brand)"><path d="M10 0a10 10 0 00-10 10c0 7.5 10 18 10 18s10-10.5 10-18A10 10 0 0010 0zm0 14a4 4 0 110-8 4 4 0 010 8z"/></svg><span>Larkfield Gardens, Elmsworth<br>Elmsworth EL18 1 United Kingdom</span></li>
    </ul>
  </div>

  <div class="abs footer-col links-col">
    <h4>Links</h4>
    <ul><li>Home</li><li>About</li><li>Services</li><li>Articles</li><li>Training</li><li>Contact us</li></ul>
  </div>

  <div class="abs footer-rule"></div>
  <p class="abs copyright">© 2023 &nbsp;All Rights Reserved | Brackwell Staffing Ltd</p>
</footer>

</body>
</html>
```